Buckslip for Eye doc

We need a simple buckslip that states info for an optometry practice.

We would like the header to be something around broken glasses, dry eyes, pink eye? Then the logo or have the logo above the text. Please look at www.cedarlineoptics.example for design options along with examples attached

Target Market(s)

Individuals staying in hotels

Industry/Entity Type

Eyewear

Font styles to use
Serif

Requirements
Must have
• Logo, map and call - out for pink eyes
Nice to have
• Image of barn for steamboat. see website, pick of the ridge logo, names are Dr. Talia Brenwick and Dr. Martin Okafor.
• This is a different business than Larkfield Optical the name of this company is Cedarline Optics located in Steamboat Springs CO

```html
<!DOCTYPE html>
<html lang="en">
<head>
<meta charset="utf-8">
<title>Cedarline Optics Buckslip</title>
<link href="https://fonts.googleapis.com/css2?family=Roboto+Condensed:wght@400;700&family=Roboto+Slab:wght@300;400;800&family=Lato:wght@400;700&family=Oswald:wght@500&family=Great+Vibes&display=swap" rel="stylesheet">
<style>
  :root{
    --red:#8f1116;
    --red-dark:#6f0f13;
    --red-bright:#b0151b;
    --ink:#2b2b2b;
    --grey-dark:#5a5a5a;
    --grey-mid:#8a8a8a;
    --black:#1c1c1c;
    --page:#d8d8d8;
    --white:#ffffff;
  }
  *{box-sizing:border-box;margin:0;padding:0}
  html,body{width:960px;height:1200px;overflow:hidden;background:var(--page)}
  .card{position:absolute;top:53px;width:425px;height:1032px;background:linear-gradient(#e9e9e9,#ffffff 30%,#f4f4f4);overflow:hidden;font-family:"Lato",sans-serif;color:var(--ink)}
  .card--front{left:42px}
  .card--back{left:500px}
  .abs{position:absolute}
  .brand{left:0;width:100%;text-align:center}
  .brand__name{font-family:"Roboto Slab",serif;font-weight:800;color:var(--red);font-size:34px;line-height:1}
  .brand__tag{font-family:"Lato",sans-serif;font-weight:700;color:var(--red-dark);font-size:9px;line-height:1.1;margin-top:6px;letter-spacing:.3px}
  .photo{background:linear-gradient(160deg,#c9c3d6,#9c96ad 60%,#6f6a7d)}
  .headline{right:31px;text-align:right;color:var(--white);font-family:"Roboto Condensed",sans-serif}
  .doctors{top:592px;left:0;width:100%;text-align:center;font-size:19px;line-height:24px;color:#333}
  .contact-table{top:661px;left:12px;width:402px;height:94px;display:flex}
  .contact-table__cell{flex:1;background:var(--grey-dark);color:var(--white);text-align:center;padding-top:17px;font-size:11.5px;line-height:18px}
  .contact-table__cell--alt{background:var(--grey-mid)}
  .contact-table__label{display:inline-block;background:var(--red-bright);border-left:4px solid var(--white);border-right:4px solid var(--white);font-family:"Roboto Condensed",sans-serif;font-weight:700;font-size:13px;padding:1px 12px;margin-bottom:8px}
  .call-pill{top:811px;left:38px;width:270px;height:84px;background:var(--white);border:2px solid #c9c9c9;border-radius:22px 0 0 22px;padding:7px 0 0 32px;font-family:"Oswald",sans-serif;line-height:34px}
  .call-pill__title{color:var(--red);font-size:27px}
  .call-pill__phone{color:#222;font-size:27px}
  .group-line{left:53px;top:930px;color:var(--white);font-family:"Roboto Slab",serif;font-weight:800;font-size:14px;line-height:20px}
  .group-line__big{font-size:17px}
  .badge{left:239px;top:799px;width:172px;height:172px}
  .footer{left:0;top:984px;width:100%;height:48px;background:var(--black);border-top:4px solid var(--white);color:var(--white);text-align:center;font-family:"Roboto Slab",serif;font-size:13px;letter-spacing:3px;line-height:44px}
  .band-title{left:0;top:52px;width:100%;height:67px;background:var(--red);color:var(--white);font-family:"Roboto Slab",serif;font-weight:300;font-size:19px;line-height:24px;text-align:center;padding-top:10px}
  .bullets{list-style:none;left:62px;width:330px;font-size:13px;line-height:16px;color:#333}
  .bullets li{position:relative;padding-left:17px}
  .bullets li::before{content:"";position:absolute;left:0;top:5px;width:8px;height:8px;border-radius:50%;background:var(--red)}
  .section-tag{left:0;top:424px;width:276px;height:35px;background:var(--red);color:var(--white);font-weight:700;font-size:19px;line-height:35px;padding-left:52px}
  .locations-box{left:80px;top:821px;width:266px;height:50px;background:var(--black);border:3px solid var(--white);color:var(--white);font-family:"Great Vibes",cursive;font-size:30px;text-align:center;line-height:44px}
  .locations{left:0;top:885px;width:100%;text-align:center;color:var(--white);font-weight:700;font-size:17px;line-height:24px}
</style>
</head>
<body>

<section class="card card--front">
  <div class="abs brand" style="top:58px">
    <div class="brand__name">Cedarline Optics</div>
    <div class="brand__tag">EXCLUSIVE EYEWEAR,<br>QUALITY EYECARE</div>
  </div>

  <svg class="abs" style="left:0;top:0" width="425" height="600" aria-hidden="true">
    <rect x="158" y="311" width="267" height="260" fill="var(--red)"/>
    <rect x="266" y="311" width="159" height="260" fill="var(--red-dark)"/>
    <rect x="0" y="543" width="158" height="28" fill="var(--red)"/>
  </svg>

  <div class="abs photo" style="left:0;top:163px;width:198px;height:408px;border-radius:90px 90px 0 0" role="img" aria-label="Young man in glasses and tie with crossed arms"></div>

  <svg class="abs" style="left:164px;top:197px" width="250" height="130" aria-hidden="true">
    <circle cx="64" cy="64" r="61" fill="#6b6b6b"/>
    <circle cx="186" cy="64" r="61" fill="#6b6b6b"/>
    <circle cx="186" cy="64" r="54" fill="var(--white)"/>
  </svg>
  <div class="abs" style="left:174px;top:207px;width:108px;height:108px;border-radius:50%;background:radial-gradient(#e7c4b0,#b88c78)" role="img" aria-label="Close-up of an eye with a contact lens"></div>
  <div class="abs" style="left:302px;top:213px;width:96px;height:96px;border-radius:50%;background:radial-gradient(#ffffff,#e4e4e4)" role="img" aria-label="Pair of rimless eyeglasses"></div>

  <div class="abs headline" style="top:350px;font-size:50px;line-height:50px">Red</div>
  <div class="abs headline" style="top:402px;font-size:70px;line-height:70px;font-weight:700">EYES?</div>
  <div class="abs" style="left:202px;top:480px;width:204px;height:3px;background:var(--white)"></div>
  <div class="abs headline" style="top:490px;font-size:33px;line-height:36px">Call our doctors</div>

  <div class="abs doctors">Owen R. Hale, O.D. Lionel T. Marsh<br>O.D. Nathan P. Ellery, O.D.</div>

  <div class="abs contact-table">
    <div class="contact-table__cell">
      <span class="contact-table__label">Dr. Hale</span><br>Home: 320-555-0117<br>Cellular:320-555-0128
    </div>
    <div class="contact-table__cell contact-table__cell--alt">
      <span class="contact-table__label">Dr. Marsh</span><br>Home: 320-555-0133<br>Cellular:320-555-0146
    </div>
    <div class="contact-table__cell">
      <span class="contact-table__label">Dr. Ellery</span><br>Home: 320-555-0159<br>Cellular:320-555-0161
    </div>
  </div>

  <svg class="abs" style="left:0;top:921px" width="425" height="60" aria-hidden="true">
    <polygon points="46,0 425,0 425,60 0,60 0,40" fill="var(--red)"/>
  </svg>
  <div class="abs group-line">Larkfield Optical Group<br><span class="group-line__big">A Regional EyeCare</span></div>

  <div class="abs call-pill">
    <div class="call-pill__title">Call Us Today</div>
    <div class="call-pill__phone">(970) 555-0142</div>
  </div>

  <svg class="abs badge" viewBox="0 0 172 172" aria-hidden="true">
    <circle cx="86" cy="86" r="85" fill="#bdbdbd"/>
    <circle cx="86" cy="86" r="80" fill="#f2f2f2"/>
    <circle cx="86" cy="86" r="76" fill="#1b1b1b"/>
    <circle cx="86" cy="86" r="70" fill="var(--white)"/>
    <text x="86" y="84" text-anchor="middle" font-family="Oswald, sans-serif" font-weight="500" font-size="36" fill="var(--red)">ON CALL</text>
    <text x="86" y="124" text-anchor="middle" font-family="Oswald, sans-serif" font-weight="500" font-size="34" fill="#111">24 hours</text>
  </svg>

  <div class="abs footer">www.cedarlineoptics.example</div>
</section>

<section class="card card--back">
  <div class="abs band-title">Larkfield Optical Group A Regional<br>EyeCare System Available Services</div>

  <ul class="abs bullets" style="top:139px">
    <li style="margin-bottom:11px">24 Hour "On Call" doctors and staff</li>
    <li style="margin-bottom:11px">Regular and emergency office calls</li>
    <li style="margin-bottom:16px">Treatment of all infections including "Pink Eye" and bacteria infections</li>
    <li style="margin-bottom:16px">Removal of foreign bodies from the eye, such as wood or metal.</li>
    <li style="margin-bottom:11px">Treatment of eye allergies or burns</li>
    <li style="margin-bottom:11px">Dry eye treatment &amp; management</li>
    <li style="margin-bottom:11px">Glaucoma treatment &amp; management</li>
    <li>LASIK consultation &amp; treatment</li>
  </ul>

  <div class="abs section-tag">What this means to you:</div>

  <ul class="abs bullets" style="top:474px">
    <li style="margin-bottom:17px">ALL your eye care in one location</li>
    <li style="margin-bottom:17px">Convenient eye care for the whole family from eye care, specialists</li>
    <li style="margin-bottom:17px">Less expensive, cost effective care</li>
    <li>Eye care you can rely on from caring doctors you know and can trust</li>
  </ul>

  <div class="abs brand" style="top:696px">
    <div class="brand__name" style="font-size:27px">Cedarline Optics</div>
    <div class="brand__tag" style="font-size:7.5px;margin-top:5px">EXCLUSIVE EYEWEAR,<br>QUALITY EYECARE</div>
  </div>

  <svg class="abs" style="left:0;top:831px" width="425" height="150" aria-hidden="true">
    <polygon points="34,0 425,0 425,150 0,150 0,36" fill="var(--red-dark)"/>
    <polygon points="34,0 124,0 124,150 0,150 0,36" fill="var(--red)"/>
  </svg>
  <div class="abs locations-box">3 Convenient locations</div>
  <div class="abs locations">Alder Bend: 763-555-0174<br>Pine Hollow 320-555-0182<br>Stone Ford: 320-555-0195</div>

  <div class="abs footer">www.cedarlineoptics.example</div>
</section>

</body>
</html>
```